Marolina Swimming & Athletics Center

We need Business Card for a Athletics center
The logo frome the Uploaded Files ( b card fimal)
Οn one side of card we need the logo of company the Contact and the website:
1. Address:(Limassol, Cyprus 12-14 Dravelonos str,Ano Feralia,P.C. 5280)

2.Phone number: (+357) 25-804273

3. Mail: info@marolinasport.example

3. Website: www.marolinasport.example

Οn the other side of the card we need to write the sport of the company:

1. Artistic Gymnastics
2. Swimming
3. Gym - Fitness
4. Programs
5. Dancing
5.Tennis

From the Uploaded Files you can get the logo.In a logo is behind the black color which can be removed from logo.

Υou can use that color you want.
.

Industry/Entity Type

Business

Font styles to use
Decorative

Colors
0555a3
ffcf3e
3176b5
0692cd
add136
f04a50
000000
cfcfcf
9d9d9d

Requirements
Should not have
• photos with faces
• photo fro the Website:www.marolinasport.example

```html
<!DOCTYPE html>
<html lang="en">
<head>
<meta charset="utf-8">
<title>Marolina Swimming &amp; Athletics Center – Business Card</title>
<link rel="stylesheet" href="https://fonts.googleapis.com/css2?family=Archivo+Black&family=Roboto:wght@300;400&display=swap">
<style>
  :root {
    --bg: #2b2e33;
    --card: #141416;
    --gold: #ffcf3e;
    --gold-deep: #f5a623;
    --white: #ffffff;
    --ink: #1c1c1c;
    --muted: #9d9d9d;
  }
  html, body {
    margin: 0;
    width: 1200px;
    height: 900px;
    overflow: hidden;
    background: var(--bg);
  }
  .stage {
    position: relative;
    width: 1200px;
    height: 900px;
  }
  .card {
    position: absolute;
    width: 540px;
    height: 310px;
    border-radius: 26px;
    background: var(--card);
    overflow: hidden;
    box-shadow: 0 18px 40px rgba(0,0,0,.45);
  }
  .card--front { left: 70px; top: 490px; }
  .card--back  { left: 590px; top: 100px; }

  .white-band {
    position: absolute;
    left: 0; right: 0; bottom: 0;
    height: 56px;
    background: var(--white);
  }

  /* front */
  .brand-name {
    position: absolute;
    left: 44px; top: 44px;
    margin: 0;
    font-family: "Archivo Black", sans-serif;
    font-size: 54px;
    letter-spacing: 1px;
    line-height: 1;
    white-space: nowrap;
    color: var(--gold);
  }
  .divider {
    position: absolute;
    left: 44px; top: 122px;
    width: 350px; height: 2px;
    background: var(--gold);
  }
  .brand-mark {
    position: absolute;
    left: 418px; top: 70px;
    width: 84px; height: 84px;
    border-radius: 50%;
    border: 3px solid var(--gold);
    box-sizing: border-box;
  }
  .contact-list {
    position: absolute;
    left: 44px; top: 146px;
    margin: 0; padding: 0;
    list-style: none;
    font-family: Roboto, sans-serif;
    font-size: 15px;
    color: var(--muted);
  }
  .contact-list li {
    display: flex;
    align-items: center;
    gap: 10px;
    height: 26px;
  }
  .icon-dot {
    width: 18px; height: 18px;
    border-radius: 50%;
    background: var(--gold);
    display: flex; align-items: center; justify-content: center;
    flex: none;
  }
  .address {
    position: absolute;
    left: 44px; bottom: 0;
    height: 56px;
    margin: 0;
    display: flex; align-items: center; gap: 10px;
    font-family: Roboto, sans-serif;
    font-size: 15px;
    white-space: nowrap;
    color: var(--ink);
  }

  /* back */
  .sports {
    position: absolute;
    left: 0; right: 0; top: 64px;
    margin: 0;
    text-align: center;
    font-family: Roboto, sans-serif;
    font-weight: 300;
    font-size: 14px;
    letter-spacing: 0.6px;
    line-height: 1.8;
    white-space: nowrap;
    color: var(--gold-deep);
    text-transform: uppercase;
  }
  .web-bar {
    position: absolute;
    left: 90px; bottom: 16px;
    width: 330px; height: 30px;
    background: var(--gold);
    display: flex; align-items: center; justify-content: center;
    font-family: Roboto, sans-serif;
    font-size: 15px;
    letter-spacing: 1px;
    color: var(--ink);
  }
</style>
</head>
<body>
<main class="stage">

  <section class="card card--front" aria-label="Card front">
    <h1 class="brand-name">MAROLINA</h1>
    <div class="divider"></div>
    <div class="brand-mark" aria-hidden="true"></div>
    <ul class="contact-list">
      <li>
        <span class="icon-dot">
          <svg width="10" height="10" viewBox="0 0 10 10"><path d="M2 1h2l1 2-1 1a5 5 0 0 0 2 2l1-1 2 1v2a1 1 0 0 1-1 1A8 8 0 0 1 1 2a1 1 0 0 1 1-1z" fill="#141416"/></svg>
        </span>
        (+357) 25-804273
      </li>
      <li>
        <span class="icon-dot">
          <svg width="10" height="8" viewBox="0 0 10 8"><rect x=".5" y=".5" width="9" height="7" fill="none" stroke="#141416"/><path d="M.5 .5 5 4.5 9.5 .5" fill="none" stroke="#141416"/></svg>
        </span>
        info@marolinasport.example
      </li>
      <li>
        <span class="icon-dot">
          <svg width="10" height="10" viewBox="0 0 10 10"><circle cx="5" cy="5" r="4.2" fill="none" stroke="#141416"/><path d="M1 5h8M5 1c-2 2.5-2 5.5 0 8M5 1c2 2.5 2 5.5 0 8" fill="none" stroke="#141416" stroke-width=".8"/></svg>
        </span>
        www.marolinasport.example
      </li>
    </ul>
    <div class="white-band"></div>
    <p class="address">
      <span class="icon-dot">
        <svg width="8" height="11" viewBox="0 0 8 11"><path d="M4 0a4 4 0 0 1 4 4c0 3-4 7-4 7S0 7 0 4a4 4 0 0 1 4-4z" fill="#fff"/><circle cx="4" cy="4" r="1.4" fill="#ffcf3e"/></svg>
      </span>
      Limassol, Cyprus 12-14 Dravelonos str,Ano Feralia,P.C. 5280
    </p>
  </section>

  <section class="card card--back" aria-label="Card back">
    <p class="sports">
      Artistic Gymnastics | Gym - Fitness<br>
      Indoor Swimming Pool | Classes | Dancing | Tennis
    </p>
    <div class="white-band"></div>
    <div class="web-bar">www.marolinasport.example</div>
  </section>

</main>
</body>
</html>
```